Australian Trucking Company Requires Professional Looking Stationary

We require a professional looking stationary design that incorporates our newly designed logo.

Our business, called "Vell Haulage Contracting", provides contracting work, transport and logistics to business in Western Australia particularly with links to the mining sector.

We are a small business looking to expand and our new logo and our new stationary will help develop our brand image in our market place.

Target Market(s)

Businesses and Corporation with links to the Mining Sector

Industry/Entity Type

Small Business

Requirements
Must have
• The letterhead must have the following details:
The new logo

Text saying: "Vell Haulage Pty Ltd (ACN 582 306 917) ATF The Vell Discretionary Trust T/AS"
"ABN 71 840 239 568"
Address "P.O Box 817 Ashbury WA, 6912"
Phone: 08 9172 5840
Email: vellhaul@mailnest.com.au

The text on the letterhead should be editable as the details are likely to change in the near future. Provision should be made for a website address all though one isn't available at the moment.

The styling, layout and font text is entirely up to the designer.

```html
<!DOCTYPE html>
<html lang="en">
<head>
<meta charset="utf-8">
<title>Vell Haulage Contracting – Letterhead</title>
<link rel="stylesheet" href="https://fonts.googleapis.com/css2?family=Open+Sans:wght@400;700&display=swap">
<style>
  :root {
    --backdrop: #1c1c1c;
    --paper: #ffffff;
    --brand-red: #c8141b;
    --band-red: #7e0b0f;
    --label-red: #ff3a3a;
    --band-text: #ffffff;
    --mark-grey: #5a5a5a;
    --truck-light: #9a9a9a;
    --truck-dark: #3c3c3c;
  }
  * { box-sizing: border-box; margin: 0; padding: 0; }
  html, body {
    width: 1018px;
    height: 1200px;
    overflow: hidden;
    background: var(--backdrop);
    font-family: "Open Sans", Arial, sans-serif;
  }
  .letterhead {
    position: absolute;
    left: 69px;
    top: 31px;
    width: 880px;
    height: 1138px;
    background: var(--paper);
    overflow: hidden;
  }
  .brand {
    position: absolute;
    left: 40px;
    top: 72px;
    display: flex;
    align-items: center;
    gap: 20px;
  }
  .brand-square {
    width: 92px;
    height: 92px;
    background: var(--mark-grey);
  }
  .brand-name {
    font-weight: 700;
    font-size: 29px;
    line-height: 30px;
    letter-spacing: 1px;
    text-transform: uppercase;
    color: var(--brand-red);
  }
  .footer-band {
    position: absolute;
    left: 0;
    bottom: 0;
    width: 100%;
    height: 69px;
    background: var(--band-red);
    color: var(--band-text);
    font-size: 12.5px;
    line-height: 17px;
  }
  .footer-col {
    position: absolute;
    top: 9px;
    white-space: nowrap;
  }
  .footer-col.company { left: 36px; }
  .footer-col.contact { left: 308px; }
  .footer-col.website {
    left: 530px;
    top: 26px;
    color: var(--label-red);
    z-index: 2;
  }
  .label { color: var(--label-red); }
  .truck-illustration {
    position: absolute;
    left: 702px;
    top: 936px;
    width: 166px;
    height: 196px;
    border-radius: 6px;
    background: linear-gradient(160deg, var(--truck-light), var(--truck-dark));
    z-index: 1;
  }
</style>
</head>
<body>
  <main class="letterhead">
    <header class="brand">
      <div class="brand-square"></div>
      <h1 class="brand-name">Vell<br>Haulage<br>Contracting</h1>
    </header>

    <footer class="footer-band">
      <div class="footer-col company">
        <span class="label">Vell Haulage Pty Ltd</span> (ACN 582 306 917)<br>
        ATF The Vell Discretionary Trust T/AS<br>
        <span class="label">ABN</span> 71 840 239 568
      </div>
      <div class="footer-col contact">
        P.O Box 817 Ashbury WA, 6912<br>
        <span class="label">P</span> 08 9172 5840<br>
        <span class="label">E</span> vellhaul@mailnest.com.au
      </div>
      <div class="footer-col website">www.vellhaulage.com.au</div>
    </footer>

    <div class="truck-illustration" role="img" aria-label="Grey illustration of a prime mover truck in motion, front three-quarter view"></div>
  </main>
</body>
</html>
```